We need a website design for a new company called Studious Baguette. We offer :
- language tutoring for scholars or adult learners
- and other educational services associated with the French language as
*online support
*and immersive language cards games as card match, dominos, puzzle and happy family cards. Studious baguette will provide immersive and playful support to all age language learners.

Target Market(s)

Parents, French educators (teachers, tutors), Language schools, students

Industry/Entity Type

Tutoring

Coding

Coded - Design and coding required

Number of Pages Required

4 page

Requirements
Must have
• Clean and elegant design. Pages should be balanced and elements pleasingly presented
• Three buckets structure

```html
<!DOCTYPE html>
<html lang="en">
<head>
<meta charset="utf-8">
<title>Studious Baguette</title>
<link href="https://fonts.googleapis.com/css2?family=Roboto:wght@300;400;500;700&display=swap" rel="stylesheet">
<style>
:root{
  --plum:#a2306d;
  --plum-dark:#8a2a5d;
  --gold:#e2aa3e;
  --ink:#333;
  --muted:#8a8a8a;
  --line:#ececec;
  --soft:#f7f7f7;
  --white:#fff;
}
*{box-sizing:border-box;margin:0;padding:0}
html,body{width:1200px;height:3371px;overflow:hidden}
body{position:relative;font-family:'Roboto',sans-serif;color:var(--ink);background:var(--white)}
.abs{position:absolute}
.btn{position:absolute;background:var(--gold);color:var(--white);font-size:14px;font-weight:500;text-transform:uppercase;display:flex;align-items:center;justify-content:center;letter-spacing:.3px}
.section-title{position:absolute;left:0;width:1200px;text-align:center;color:var(--plum);font-size:29px;font-weight:500;text-transform:uppercase}
.section-sub{position:absolute;left:0;width:1200px;text-align:center;color:var(--muted);font-size:14px;font-weight:300}
.photo{position:absolute}

/* hero */
.hero{left:0;top:0;width:1200px;height:622px;background:linear-gradient(135deg,#b9a99a 0%,#e7e2dc 35%,#cfc2b4 60%,#7c6a5a 100%)}
.nav{left:130px;top:27px;width:937px;height:97px;background:var(--white);display:flex;align-items:center}
.logo{display:flex;align-items:center;gap:10px;color:var(--plum);font-weight:500;font-size:21px}
.logo-mark{width:18px;height:18px;background:var(--gold)}
.nav .logo{position:absolute;left:26px;top:34px}
.nav-link{position:absolute;top:66px;font-size:14px;font-weight:500;color:#222;text-transform:uppercase}
.nav-link.active{color:var(--plum)}
.nav-link.active::after{content:"";position:absolute;left:-4px;right:-4px;top:30px;height:2px;background:var(--plum)}
.caption{left:0;top:546px;width:1200px;height:76px;background:rgba(120,30,85,.72)}
.caption-text{position:absolute;left:268px;top:28px;color:var(--white);font-size:18px;text-transform:uppercase}
.arrow{position:absolute;color:var(--white)}

/* welcome */
.welcome-copy{left:220px;top:756px;width:760px;text-align:center;color:var(--muted);font-size:14px;line-height:28px;font-weight:300}

/* buckets */
.bucket{position:absolute;top:1011px;width:290px;height:459px;background:#fbfbfb;border:1px solid var(--line)}
.bucket svg{position:absolute;left:31px;top:72px}
.bucket h3{position:absolute;left:29px;top:147px;color:var(--plum);font-size:23px;font-weight:500;line-height:27px;text-transform:uppercase}
.bucket p{position:absolute;left:29px;top:254px;width:240px;color:var(--muted);font-size:14px;line-height:24px;font-weight:300}
.bucket .btn{left:27px;top:379px;width:132px;height:42px}

/* topics */
.topic{position:absolute;top:1701px;width:289px}
.topic .photo{position:relative;width:289px;height:193px}
.topic h4{margin-top:39px;color:var(--plum);font-size:14px;font-weight:400;text-transform:uppercase}
.topic p{margin-top:12px;color:var(--muted);font-size:14px;line-height:25px;font-weight:300}

/* games */
.games{left:0;top:2112px;width:1200px;height:393px;background:var(--soft);border-top:1px solid var(--line)}
.game{position:absolute;top:2278px;width:209px}
.game .photo{position:relative;width:209px;height:138px}
.game span{display:block;margin-top:26px;text-align:center;font-size:14px;text-transform:uppercase;color:#333}

/* stories */
.stories{left:0;top:2505px;width:1200px;height:481px;background:linear-gradient(180deg,#a3427a,#9b3a72)}
.stories .section-title{color:var(--white);top:79px;font-size:28px}
.avatar{position:absolute;top:196px;width:134px;height:134px;border-radius:50%;background:linear-gradient(160deg,#c7b2a4,#e8ddd6);border:3px solid var(--white)}
.quote{position:absolute;top:222px;color:var(--white);font-size:68px;font-weight:700;line-height:60px;font-family:Georgia,serif}
.name{position:absolute;top:218px;color:var(--white);font-size:29px;font-weight:300}
.story{position:absolute;top:270px;width:296px;color:var(--white);font-size:12px;line-height:21px;font-weight:300}

/* footer */
.footer-logo{left:130px;top:3150px}
.foot-title{position:absolute;top:3030px;color:var(--plum);font-size:15px;text-transform:uppercase;padding-bottom:14px;border-bottom:2px solid var(--plum);font-weight:400}
.links{position:absolute;left:383px;top:3100px;list-style:none}
.links li{font-size:13px;color:#333;line-height:29.5px}
.links li::before{content:"›";margin-right:8px}
.contact-item{position:absolute;left:539px;display:flex;gap:20px}
.contact-icon{width:32px;height:32px;border:2px solid var(--plum);border-radius:50%;display:flex;align-items:center;justify-content:center;flex:none}
.contact-item div.text{font-size:11px;line-height:18px;color:#333}
.contact-item b{font-weight:500;text-transform:uppercase}
.field{position:absolute;border:1px solid #bbb;background:var(--white);font-size:10px;color:#777;padding:8px 10px}
.send{position:absolute;left:800px;top:3212px;width:110px;height:37px;background:var(--plum);color:var(--white);font-size:11px;display:flex;align-items:center;justify-content:center;text-transform:uppercase}
.bottom{left:0;top:3303px;width:1200px;height:68px;background:var(--soft)}
.copyright{position:absolute;left:132px;top:26px;font-size:12px;color:#333}
.social{position:absolute;top:18px;width:34px;height:34px;border:2px solid var(--plum);border-radius:50%}
</style>
</head>
<body>

<header class="abs hero" role="img" aria-label="Photo of a smiling tutor teaching a group of students in a classroom"></header>
<nav class="abs nav">
  <div class="logo"><span class="logo-mark"></span>Studious Baguette</div>
  <span class="nav-link active" style="left:367px;top:39px">Home</span>
  <span class="nav-link" style="left:465px;top:39px">About Us</span>
  <span class="nav-link" style="left:591px;top:39px">Courses</span>
  <span class="nav-link" style="left:715px;top:39px">Services</span>
  <span class="nav-link" style="left:838px;top:39px">Contact Us</span>
</nav>
<div class="abs caption">
  <svg class="arrow" style="left:70px;top:30px" width="12" height="16" viewBox="0 0 12 16"><path d="M9 2 3 8l6 6" fill="none" stroke="#fff" stroke-width="2.5"/></svg>
  <span class="caption-text">Language tutoring for scholars or adult learners</span>
  <span class="btn" style="left:798px;top:18px;width:130px;height:40px">Learn More</span>
  <svg class="arrow" style="left:1147px;top:30px" width="12" height="16" viewBox="0 0 12 16"><path d="M3 2l6 6-6 6" fill="none" stroke="#fff" stroke-width="2.5"/></svg>
</div>

<section>
  <h1 class="section-title" style="top:688px">Welcome to Studious Baguette</h1>
  <p class="abs welcome-copy">Lorem ipsum dolor sit amet, consectetur adipiscing elit, sed do eiusmod tempor incididunt ut labore et dolore magna aliqua. Ut enim ad minim veniam, quis nostrud exercitation ullamco laboris nisi ut aliquip ex ea commodo consequat. Duis aute irure dolor in reprehenderit in voluptate velit esse cillum dolore eu fugiat nulla pariatur.</p>
  <span class="btn" style="left:534px;top:867px;width:132px;height:41px">Learn More</span>
</section>

<section>
  <article class="bucket" style="left:142px">
    <svg width="74" height="50" viewBox="0 0 74 50"><path d="M37 4 2 18l35 14 35-14z" fill="#333"/><path d="M16 24v14c8 7 34 7 42 0V24L37 32z" fill="#333"/><path d="M68 19v18" stroke="#333" stroke-width="3"/></svg>
    <h3>Higher<br>Studies<br>Education</h3>
    <p>Lorem ipsum dolor sit amet, consectetur adipiscing elit, sed do eiusmod tempor incididunt ut labore et dolore magna aliqua.</p>
    <span class="btn">Learn More</span>
  </article>
  <article class="bucket" style="left:454px">
    <svg width="60" height="54" viewBox="0 0 60 54"><path d="M18 4h34L40 48H6z" fill="none" stroke="#333" stroke-width="5" stroke-linejoin="round"/><path d="M22 16h20M19 26h20" stroke="#333" stroke-width="4"/><path d="M6 48h34" stroke="#333" stroke-width="5"/></svg>
    <h3>Language<br>Tutoring<br>for Scholars</h3>
    <p>Lorem ipsum dolor sit amet, consectetur adipiscing elit, sed do eiusmod tempor incididunt ut labore et dolore magna aliqua.</p>
    <span class="btn">Learn More</span>
  </article>
  <article class="bucket" style="left:766px">
    <svg width="60" height="50" viewBox="0 0 60 50"><rect x="3" y="5" width="54" height="40" rx="3" fill="none" stroke="#333" stroke-width="5"/><path d="M12 16h5M22 16h26M12 25h5M22 25h26M12 34h5M22 34h26" stroke="#333" stroke-width="4"/></svg>
    <h3>Immersive<br>Language<br>Cards Game</h3>
    <p>Lorem ipsum dolor sit amet, consectetur adipiscing elit, sed do eiusmod tempor incididunt ut labore et dolore magna aliqua.</p>
    <span class="btn">Learn More</span>
  </article>
</section>

<section>
  <h2 class="section-title" style="top:1574px">Learners Course</h2>
  <p class="section-sub" style="top:1619px">Lorem ipsum dolor sit amet, consectetur adipiscing elit, sed do eiusmod tempor</p>
  <article class="topic" style="left:143px">
    <div class="photo" role="img" aria-label="Photo of a young student writing at a desk" style="background:linear-gradient(135deg,#d9c0a8,#b97a7a)"></div>
    <h4>Featured Topic 1</h4>
    <p>Lorem ipsum dolor sit amet, consectetur adipiscing elit, sedt do eiusmod tempor incididunt ut labore et dolore ...</p>
  </article>
  <article class="topic" style="left:455px">
    <div class="photo" role="img" aria-label="Photo of two children doing a science experiment" style="background:linear-gradient(135deg,#3f7f7a,#d7b36a 70%,#c84b7c)"></div>
    <h4>Featured Topic 2</h4>
    <p>Lorem ipsum dolor sit amet, consectetur adipiscing elit, sedt do eiusmod tempor incididunt ut labore et dolore ...</p>
  </article>
  <article class="topic" style="left:767px">
    <div class="photo" role="img" aria-label="Photo of a woman holding a French flag outdoors" style="background:linear-gradient(135deg,#8fae6a,#3e4f9a 45%,#e8e2e0 60%,#c8404a)"></div>
    <h4>Featured Topic 3</h4>
    <p>Lorem ipsum dolor sit amet, consectetur adipiscing elit, sedt do eiusmod tempor incididunt ut labore et dolore ...</p>
  </article>
</section>

<section class="abs games"></section>
<h2 class="section-title" style="top:2178px">Language Cards Games</h2>
<p class="section-sub" style="top:2223px">Lorem ipsum dolor sit amet, consectetur adipiscing elit, sed do eiusmod tempor</p>
<div class="game" style="left:144px"><div class="photo" role="img" aria-label="Photo of playing cards and chips" style="background:linear-gradient(135deg,#7a1010,#3a0808)"></div><span>Card Match</span></div>
<div class="game" style="left:377px"><div class="photo" role="img" aria-label="Photo of dominoes on a table" style="background:linear-gradient(135deg,#6b4a30,#c39a6a)"></div><span>Dominos</span></div>
<div class="game" style="left:611px"><div class="photo" role="img" aria-label="Photo of hands assembling a puzzle" style="background:linear-gradient(135deg,#6fa8a8,#d8b88a)"></div><span>Puzzle</span></div>
<div class="game" style="left:847px"><div class="photo" role="img" aria-label="Photo of a girl playing a family card game" style="background:linear-gradient(135deg,#c08a60,#5a7080)"></div><span>Happy Family Cards</span></div>

<section class="abs stories" role="region" aria-label="Success stories">
  <h2 class="section-title">Success Stories</h2>
  <div class="avatar" style="left:151px" role="img" aria-label="Portrait of a smiling male learner"></div>
  <span class="quote" style="left:304px">&ldquo;</span>
  <span class="name" style="left:375px">Daniel Forbes</span>
  <p class="story" style="left:307px">Lorem ipsum dolor sit amet, consectetur adipiscing elit, sed do eiusmod tempor incididunt ut labore et dolore magna aliqua. Ut enim ad minim veniam, quis nostrud exercitation ullamco laboris nisi</p>
  <div class="avatar" style="left:627px" role="img" aria-label="Portrait of a smiling female learner"></div>
  <span class="quote" style="left:776px">&ldquo;</span>
  <span class="name" style="left:846px">Clara Whitmore</span>
  <p class="story" style="left:778px">Lorem ipsum dolor sit amet, consectetur adipiscing elit, sed do eiusmod tempor incididunt ut labore et dolore magna aliqua. Ut enim ad minim veniam, quis nostrud exercitation ullamco laboris nisi</p>
  <svg class="abs" style="left:569px;top:412px" width="14" height="20" viewBox="0 0 14 20"><path d="M11 2 3 10l8 8" fill="none" stroke="#fff" stroke-width="3"/></svg>
  <svg class="abs" style="left:615px;top:412px" width="14" height="20" viewBox="0 0 14 20"><path d="M3 2l8 8-8 8" fill="none" stroke="#fff" stroke-width="3"/></svg>
</section>

<footer>
  <div class="abs logo footer-logo"><span class="logo-mark"></span>Studious Baguette</div>
  <h4 class="foot-title" style="left:382px">Quick Links</h4>
  <ul class="links">
    <li>Home</li><li>Courses</li><li>Features</li><li>Events</li><li>Languages</li><li>Contact Us</li>
  </ul>
  <h4 class="foot-title" style="left:539px">Contact Us</h4>
  <div class="contact-item" style="top:3100px">
    <span class="contact-icon"><svg width="12" height="16" viewBox="0 0 12 16"><path d="M6 15S1 9 1 6a5 5 0 0 1 10 0c0 3-5 9-5 9z" fill="none" stroke="#a2306d" stroke-width="1.6"/><circle cx="6" cy="6" r="1.8" fill="#a2306d"/></svg></span>
    <div class="text"><b>Studious Baguette</b><br>48 Linden Row<br>200 Maplebrook, AZ 54321</div>
  </div>
  <div class="contact-item" style="top:3166px">
    <span class="contact-icon"><svg width="10" height="16" viewBox="0 0 10 16"><rect x="1" y="1" width="8" height="14" rx="1.5" fill="none" stroke="#a2306d" stroke-width="1.6"/><circle cx="5" cy="12" r="1" fill="#a2306d"/></svg></span>
    <div class="text"><b>Phone</b><br>180 555 0147</div>
  </div>
  <div class="contact-item" style="top:3228px">
    <span class="contact-icon"><svg width="14" height="10" viewBox="0 0 14 10"><rect x="0" y="0" width="14" height="10" rx="1" fill="#a2306d"/><path d="M0 1l7 5 7-5" fill="none" stroke="#fff" stroke-width="1.2"/></svg></span>
    <div class="text"><b>Mail</b><br>info@studiousbaguette.com</div>
  </div>
  <h4 class="foot-title" style="left:800px">Contact Form</h4>
  <div class="field" style="left:800px;top:3098px;width:127px;height:31px">Name</div>
  <div class="field" style="left:939px;top:3098px;width:128px;height:31px">Phone</div>
  <div class="field" style="left:800px;top:3140px;width:267px;height:57px">Message</div>
  <span class="send">Send Message</span>
  <div class="abs bottom">
    <span class="copyright">Copyright &copy; 2017 Studious Baguette. All Rights Reserved.</span>
    <span class="social" style="left:855px"></span>
    <span class="social" style="left:899px"></span>
    <span class="social" style="left:943px"></span>
    <span class="social" style="left:987px"></span>
    <span class="social" style="left:1031px"></span>
  </div>
</footer>

</body>
</html>
```